Harold The Realtor Business Card Design

I need a new card design for my real estate business in Seattle Wa. I am interested in a unique design. My business revolves around my personal services and I want the card to show professionalism, creativity and good execution. I specialize in residential real estate in Maple ridge / downtown neighborhoods. The card is my first impression on may of my clients and in the service industry any time you can stand out from the crowd and make an impression will go a long way.

Target Market(s)

I will be handing the card to prospects/ potential buyers and sellers of residential real estate.

Industry/Entity Type

Real Estate Agent

Contact Information for Business Card

Email: Info@Haroldtherealtor.com Website: HaroldtheRealtor.com Cell phone: 206-555-0184 Fax 206-555-0127

Font styles to use
Sans Serif

Colors
0255a3
ffc214

Requirements
Must have
• I will need to have my firms logo "Keystone 8" and my logo "HTR" on the business card. I would like to have my firms logo smaller then mine. I would also like to have my photo on the card. By business colors are gold and white with blue accents.
Nice to have
• It would be nice to have a unique shape or feel (texture) rather then your standard business card. I saw cardly press had metal cards which could be interesting.

```html
<!DOCTYPE html>
<html lang="en">
<head>
<meta charset="utf-8">
<title>Harold The Realtor – Business Card</title>
<link href="https://fonts.googleapis.com/css2?family=Montserrat:wght@700&family=Source+Sans+3:wght@400&display=swap" rel="stylesheet">
<style>
  :root {
    --frame-blue: #2c5a92;
    --band-gold: #cfae52;
    --logo-bronze: #85622a;
    --text-grey: #595959;
    --paper: #ffffff;
    --page: #ffffff;
  }
  html, body {
    margin: 0;
    width: 1183px;
    height: 1200px;
    overflow: hidden;
    background: var(--page);
  }
  .sheet {
    position: relative;
    width: 1183px;
    height: 1200px;
  }
  .card {
    position: absolute;
    top: 385px;
    width: 430px;
    height: 430px;
    box-sizing: border-box;
    border: 21px solid var(--frame-blue);
    background: var(--paper);
    box-shadow: 0 1px 3px rgba(0,0,0,0.25);
  }
  .card--front { left: 90px; }
  .card--back { left: 657px; }

  .brand-mark {
    font-family: "Montserrat", sans-serif;
    font-weight: 700;
    color: var(--logo-bronze);
    text-align: center;
    line-height: 1.05;
  }
  .brand-mark__square {
    display: block;
    margin: 0 auto 12px;
    background: var(--logo-bronze);
  }
  .card--front .brand-mark {
    position: absolute;
    left: 0; right: 0;
    top: 118px;
    font-size: 38px;
  }
  .card--front .brand-mark__square { width: 34px; height: 34px; }

  .card--back .brand-mark {
    position: absolute;
    left: 0; right: 0;
    top: 28px;
    font-size: 29px;
  }
  .card--back .brand-mark__square { width: 26px; height: 26px; margin-bottom: 9px; }

  .name-band {
    position: absolute;
    left: 0; right: 0;
    top: 173px;
    height: 56px;
    background: var(--band-gold);
  }
  .agent-name {
    position: absolute;
    left: 154px;
    top: 173px;
    height: 56px;
    line-height: 56px;
    font-family: "Montserrat", sans-serif;
    font-weight: 700;
    font-size: 22px;
    color: var(--paper);
  }
  .agent-photo {
    position: absolute;
    left: 24px;
    top: 152px;
    width: 108px;
    height: 100px;
    box-sizing: border-box;
    border: 3px solid var(--band-gold);
    background: linear-gradient(160deg, #e8e6e2 0%, #c9c4bc 45%, #3a3f52 100%);
  }
  .contact-list {
    position: absolute;
    left: 24px;
    top: 277px;
    margin: 0;
    padding: 0;
    list-style: none;
    font-family: "Source Sans 3", sans-serif;
    font-size: 18px;
    color: var(--text-grey);
  }
  .contact-list li {
    display: flex;
    align-items: center;
    height: 25px;
  }
  .contact-icon {
    width: 18px;
    height: 18px;
    margin-right: 11px;
    flex: none;
  }
  .firm-mark {
    position: absolute;
    right: 22px;
    bottom: 24px;
    display: flex;
    align-items: center;
    font-family: "Montserrat", sans-serif;
    font-weight: 700;
    font-size: 17px;
    color: var(--text-grey);
  }
  .firm-mark__dot {
    width: 24px;
    height: 24px;
    margin-left: 6px;
    border-radius: 50%;
    background: #8c1c1c;
  }
</style>
</head>
<body>
<main class="sheet">
  <section class="card card--front" aria-label="Card front">
    <div class="brand-mark">
      <span class="brand-mark__square"></span>
      Harold<br>The Realtor
    </div>
  </section>

  <section class="card card--back" aria-label="Card back">
    <div class="brand-mark">
      <span class="brand-mark__square"></span>
      Harold The Realtor
    </div>
    <div class="name-band"></div>
    <div class="agent-photo" role="img" aria-label="Portrait photo of the agent"></div>
    <div class="agent-name">Marisol Vega</div>

    <ul class="contact-list">
      <li>
        <svg class="contact-icon" viewBox="0 0 18 18"><rect width="18" height="18" fill="var(--band-gold)"/><rect x="3" y="5" width="12" height="8" fill="none" stroke="#fff" stroke-width="1.3"/><path d="M3 5 L9 10 L15 5" fill="none" stroke="#fff" stroke-width="1.3"/></svg>
        Info@Haroldtherealtor.com
      </li>
      <li>
        <svg class="contact-icon" viewBox="0 0 18 18"><rect width="18" height="18" fill="var(--band-gold)"/><circle cx="9" cy="9" r="5.5" fill="none" stroke="#fff" stroke-width="1.2"/><ellipse cx="9" cy="9" rx="2.3" ry="5.5" fill="none" stroke="#fff" stroke-width="1"/><path d="M3.5 9 H14.5" stroke="#fff" stroke-width="1"/></svg>
        HaroldtheRealtor.com
      </li>
      <li>
        <svg class="contact-icon" viewBox="0 0 18 18"><rect width="18" height="18" fill="var(--band-gold)"/><rect x="5.5" y="3" width="7" height="12" rx="1" fill="none" stroke="#fff" stroke-width="1.3"/><circle cx="9" cy="13" r="0.8" fill="#fff"/></svg>
        206-555-0184
      </li>
      <li>
        <svg class="contact-icon" viewBox="0 0 18 18"><rect width="18" height="18" fill="var(--band-gold)"/><rect x="3" y="7" width="12" height="8" fill="none" stroke="#fff" stroke-width="1.3"/><rect x="6" y="3" width="6" height="4" fill="none" stroke="#fff" stroke-width="1.2"/><path d="M5 10 H9 M5 12 H9" stroke="#fff" stroke-width="1"/></svg>
        206-555-0127
      </li>
    </ul>

    <div class="firm-mark">Keystone 8<span class="firm-mark__dot"></span></div>
  </section>
</main>
</body>
</html>
```